cargo van wrap for home buildedr

New service van wrap. its a corvan k340 I will attach the templet for correct sizing in the link https://files.nuvalink-box.net/item/r8QmT2xLp7ZkW4nVbY0aHs3cUe9jD5gF/open?src=mail_share_x&key=PwLx7Ra&tm=73914826
we are a custom home builder in lees summit mo
the black and gold log we have home pictures we can put into vans
i will send pics of some of our other trucks and logo does not need to look like the old ones just for reference

Target Market(s)

home buyers

Industry/Entity Type

home builder

Font styles to use
Sans Serif

Requirements
Must have
• picture of home and logo

```html
<!DOCTYPE html>
<html lang="en">
<head>
<meta charset="utf-8">
<title>Brantley Homes – Cargo Van Wrap</title>
<link href="https://fonts.googleapis.com/css2?family=Poppins:wght@600;700&display=swap" rel="stylesheet">
<style>
  :root {
    --page: #ffffff;
    --wrap-white: #fbfbfa;
    --gold: #a89260;
    --gold-dark: #8d7a4c;
    --black: #161616;
    --ink: #1b1b1b;
    --photo-top: #ecebe7;
    --photo-mid: #c9c6bf;
    --photo-floor: #7a5a3c;
  }
  html, body {
    margin: 0;
    width: 1200px;
    height: 1200px;
    overflow: hidden;
    background: var(--page);
  }
  .canvas {
    position: relative;
    width: 1200px;
    height: 1200px;
  }
  .wrap-side {
    position: absolute;
    left: 50px;
    top: 370px;
    width: 1100px;
    height: 460px;
  }
  .wrap-side svg { display: block; }
  .wrap-text { font-family: "Poppins", sans-serif; }
  .brand-name {
    fill: var(--gold);
    font-weight: 700;
    font-size: 56px;
    letter-spacing: 4px;
  }
  .brand-sub {
    fill: var(--gold);
    font-weight: 700;
    font-size: 26px;
    letter-spacing: 8px;
  }
  .phone {
    fill: var(--ink);
    font-weight: 700;
    font-size: 36px;
    letter-spacing: 1px;
  }
  .services {
    fill: var(--gold-dark);
    font-weight: 700;
    font-size: 16px;
  }
  .website {
    fill: #ffffff;
    font-weight: 600;
    font-size: 17px;
    letter-spacing: 2px;
  }
  .social-dot { fill: var(--black); }
</style>
</head>
<body>
<main class="canvas">
  <section class="wrap-side" aria-label="Brantley Homes cargo van side wrap">
    <svg width="1100" height="460" viewBox="0 0 1100 460" xmlns="http://www.w3.org/2000/svg">
      <defs>
        <linearGradient id="kitchenTones" x1="0" y1="0" x2="0" y2="1">
          <stop offset="0" stop-color="var(--photo-top)"/>
          <stop offset="0.55" stop-color="var(--photo-mid)"/>
          <stop offset="0.8" stop-color="#9b8a76"/>
          <stop offset="1" stop-color="var(--photo-floor)"/>
        </linearGradient>
      </defs>

      <rect class="panel-base" x="0" y="0" width="1100" height="300" fill="var(--wrap-white)"/>

      <rect class="home-photo" x="0" y="0" width="620" height="300" fill="url(#kitchenTones)"
            role="img" aria-label="Photo of a finished custom home kitchen with white cabinets, island, stools and wood floor"/>

      <ellipse class="logo-field" cx="840" cy="140" rx="520" ry="200"
               fill="var(--wrap-white)" stroke="var(--gold)" stroke-width="12"/>

      <rect class="lower-band" x="0" y="300" width="1100" height="160" fill="var(--black)"/>

      <rect class="gold-stripe" x="290" y="365" width="540" height="26" fill="var(--gold)"/>

      <g class="logo-rules">
        <rect x="410" y="28" width="340" height="5" fill="var(--gold)"/>
        <rect x="410" y="208" width="340" height="5" fill="var(--gold)"/>
      </g>

      <g class="wrap-text">
        <text class="brand-name" x="580" y="100" text-anchor="middle">BRANTLEY</text>
        <text class="brand-sub" x="584" y="160" text-anchor="middle">HOMES</text>

        <text class="phone" x="450" y="272">816-555-0142</text>

        <text class="services" x="738" y="262">Custom Homes | Remodel</text>
        <text class="services" x="748" y="284">Painting | Commercial</text>

        <text class="website" x="455" y="326">www.brantleybuilders.com</text>
      </g>

      <g class="social-links">
        <circle class="social-dot" cx="985" cy="268" r="10"/>
        <circle class="social-dot" cx="1015" cy="268" r="10"/>
        <circle class="social-dot" cx="1045" cy="268" r="10"/>
      </g>
    </svg>
  </section>
</main>
</body>
</html>
```